IV Bag Graphic for IV Therapy Bar

Hello we are offering an IV Therapy Bar to our medical practice. We already have a logo would like a cool design label for the IV bag. We will utilize this label for social media advertising, a sticker for the saline bag and marketing material. Woukd like something unique, sharp, bold and professional. We signed up for the Social Media package so the design will need to hold and be creative.

Target Market(s)

25-35 yrs old

Requirements
Must have
• Bellwood Clinical Research name and logo- Clear inference it is IV therapy
Nice to have
• Innovation- Lines to write Name - Also please give examples of the different IV therapies (Myers cocktail) etc (screenshot example of therapies is attached)
Should not have
• In the attached examples the packaging and label are black, in open.

```html
<!DOCTYPE html>
<html lang="en">
<head>
<meta charset="utf-8">
<title>Bellwood Clinical Research – Myers Cocktail IV Label</title>
<link rel="stylesheet" href="https://fonts.googleapis.com/css2?family=Montserrat:wght@500;600;700;800;900&display=swap">
<style>
  :root {
    --stage: #e4e4e4;
    --paper: #ffffff;
    --navy: #0b4f9c;
    --blue: #0f7fd6;
    --sky: #1a95e6;
    --orange: #ec9124;
    --ink: #2a2f3a;
    --rule: #d9dde3;
  }
  * { margin: 0; padding: 0; box-sizing: border-box; }
  html, body { width: 1200px; height: 963px; overflow: hidden; }
  body {
    background: var(--stage);
    font-family: "Montserrat", sans-serif;
    position: relative;
  }
  .label {
    position: absolute;
    left: 283px; top: 31px;
    width: 634px; height: 900px;
    background: linear-gradient(135deg, #f3f4f6 0%, var(--paper) 40%, #f7f8fa 100%);
    box-shadow: 0 4px 14px rgba(0,0,0,.22);
    overflow: hidden;
  }
  .brand {
    position: absolute; left: 67px; top: 46px;
    display: flex; align-items: center; gap: 18px;
  }
  .brand-dot {
    width: 94px; height: 94px; border-radius: 50%;
    background: var(--blue); flex: none;
  }
  .brand-name {
    color: var(--navy); font-weight: 700; line-height: 1;
  }
  .brand-name .line-main { display: block; font-size: 66px; letter-spacing: -1px; }
  .brand-name .line-sub { display: block; font-size: 29px; margin-top: 6px; letter-spacing: .3px; }
  .therapy-title {
    position: absolute; left: 61px; top: 166px;
    font-weight: 900; line-height: 93px;
    background: linear-gradient(90deg, var(--navy) 0%, var(--blue) 70%, var(--sky) 100%);
    -webkit-background-clip: text; background-clip: text; color: transparent;
  }
  .therapy-title span { display: block; font-size: 100px; letter-spacing: -3px; white-space: nowrap; }
  .pill {
    position: absolute; left: 54px; top: 375px;
    width: 519px; height: 52px; border-radius: 26px;
    background: var(--orange); color: #fff;
    font-weight: 700; font-size: 35px; letter-spacing: .5px;
    display: flex; align-items: center; justify-content: center;
    white-space: nowrap;
  }
  .ingredients {
    position: absolute; left: 47px; top: 459px; width: 278px;
    list-style: none;
  }
  .ingredients li {
    height: 42px; display: flex; align-items: center; gap: 12px;
    font-size: 24px; font-weight: 500; color: var(--ink);
    border-bottom: 1px solid var(--rule);
    white-space: nowrap;
  }
  .ingredients li:last-child { border-bottom: none; }
  .ingredients li::before {
    content: ""; width: 10px; height: 10px; border-radius: 50%;
    background: var(--orange); flex: none; margin-left: 4px;
  }
  .feature-art {
    position: absolute; left: 335px; top: 446px;
    width: 299px; height: 299px;
    background: radial-gradient(circle at 60% 50%, rgba(26,149,230,.22), rgba(236,145,36,.12) 55%, rgba(255,255,255,0) 75%);
  }
  .features {
    position: absolute; left: 0; top: 745px;
    width: 634px; height: 75px;
    background: linear-gradient(90deg, var(--navy), var(--blue) 55%, var(--navy));
    display: flex; align-items: center; padding-left: 28px;
  }
  .feature {
    display: flex; align-items: center; gap: 9px;
    color: #fff; font-weight: 700; font-size: 21px; line-height: 1.1;
    white-space: nowrap;
  }
  .feature-icon { width: 52px; height: 52px; flex: none; }
  .divider {
    width: 1px; height: 46px; background: rgba(255,255,255,.6);
    margin: 0 12px;
  }
  .volume {
    position: absolute; left: 61px; top: 836px;
    font-weight: 900; font-size: 31px; color: var(--orange);
  }
</style>
</head>
<body>
  <main class="label">
    <header class="brand">
      <div class="brand-dot"></div>
      <div class="brand-name">
        <span class="line-main">BELLWOOD</span>
        <span class="line-sub">CLINICAL RESEARCH</span>
      </div>
    </header>

    <h1 class="therapy-title">
      <span>MYERS</span>
      <span>COCKTAIL</span>
    </h1>

    <div class="pill">IV THERAPY TREATMENT</div>

    <ul class="ingredients">
      <li>Calcium Chloride</li>
      <li>Magnesium Chloride</li>
      <li>Vitamin-B Complex</li>
      <li>Vitamin-B 12</li>
      <li>Vitamin C</li>
      <li>Folic Acid</li>
    </ul>

    <div class="feature-art" role="img" aria-label="Large brand emblem decoration in blue, orange and purple"></div>

    <section class="features">
      <div class="feature">
        <svg class="feature-icon" viewBox="0 0 52 52" aria-hidden="true">
          <circle cx="26" cy="26" r="24" fill="#ec9124" stroke="#fff" stroke-width="2"/>
          <path d="M14 34 h8 l8 -4 h8" fill="none" stroke="#fff" stroke-width="3" stroke-linecap="round"/>
          <path d="M27 26 c0 -8 6 -12 12 -12 c0 7 -5 12 -12 12z" fill="#fff"/>
        </svg>
        <span>Natural<br>Therapy</span>
      </div>
      <div class="divider"></div>
      <div class="feature">
        <svg class="feature-icon" viewBox="0 0 52 52" aria-hidden="true">
          <circle cx="26" cy="26" r="24" fill="#ec9124" stroke="#fff" stroke-width="2"/>
          <path d="M13 25 h26 a13 11 0 0 1 -26 0z" fill="#fff"/>
          <path d="M28 23 l9 -10" stroke="#fff" stroke-width="3" stroke-linecap="round"/>
        </svg>
        <span>Quality<br>Ingredients</span>
      </div>
      <div class="divider"></div>
      <div class="feature">
        <svg class="feature-icon" viewBox="0 0 52 52" aria-hidden="true">
          <circle cx="26" cy="26" r="24" fill="#ec9124" stroke="#fff" stroke-width="2"/>
          <circle cx="26" cy="22" r="9" fill="none" stroke="#fff" stroke-width="3"/>
          <path d="M20 30 l-3 11 l5 -2 l3 4 l1 -11 M32 30 l3 11 l-5 -2 l-3 4" fill="none" stroke="#fff" stroke-width="2.5" stroke-linejoin="round"/>
        </svg>
        <span>Product of<br>Corvana</span>
      </div>
    </section>

    <div class="volume">1000ML</div>
  </main>
</body>
</html>
```